Redesign brightlens.net home page

We want to improve our website design overall, show us what you can do with our home page and we will move forward with the best designer to redo the other pages on our site.

Particularly interested in redesigning the header/footer.

Target Market(s)

scientists and engineers

Number of Pages Required

1 page

Font styles to use
Sans Serif

Requirements
Nice to have
• More grey and red and less black than we have now for the header

```html
<!DOCTYPE html>
<html lang="en">
<head>
<meta charset="utf-8">
<title>Brightlens Optics Corporation</title>
<link href="https://fonts.googleapis.com/css2?family=Roboto:wght@400;500;700&family=Nothing+You+Could+Do&display=swap" rel="stylesheet">
<style>
:root{
  --red:#c80c0c;
  --red-dark:#a80808;
  --grey-bg:#f4f5f7;
  --ink:#222;
  --muted:#666;
  --line:#dcdcdc;
  --white:#fff;
}
*{box-sizing:border-box;margin:0;padding:0}
html,body{width:1200px;height:2281px;overflow:hidden}
body{font-family:"Roboto",Arial,sans-serif;color:var(--ink);background:var(--white);position:relative}
.hero{position:absolute;left:0;top:0;width:1200px;height:545px;overflow:hidden}
.hero-visual{position:absolute;inset:0;background:linear-gradient(115deg,#a59a84 0%,#7b7463 38%,#5e6a7a 50%,#33507a 70%,#6c85a8 100%)}
.hero-shade{position:absolute;inset:0;background:rgba(20,25,35,.25)}
.site-header{position:absolute;left:0;top:0;width:1200px;height:67px;border-bottom:1px solid rgba(255,255,255,.35)}
.brand{position:absolute;left:46px;top:18px;display:flex;align-items:center;gap:10px;color:var(--white);font-weight:700;font-size:20px;letter-spacing:.5px}
.brand-mark{width:26px;height:26px;background:var(--red)}
.main-nav{position:absolute;top:25px;left:0}
.main-nav a{position:absolute;color:var(--white);text-decoration:none;font-size:15px;font-weight:500;white-space:nowrap}
.header-btn{position:absolute;top:16px;height:33px;border-radius:17px;font-size:13px;font-weight:500;display:flex;align-items:center;justify-content:center}
.btn-contact{left:935px;width:92px;border:2px solid var(--white);color:var(--white)}
.btn-quote{left:1034px;width:119px;background:var(--white);color:var(--ink)}
.hero-title{position:absolute;top:190px;left:0;width:1200px;text-align:center;font-family:"Nothing You Could Do",cursive;color:var(--white);font-size:46px;line-height:50px}
.hero-text{position:absolute;top:322px;left:0;width:1200px;text-align:center;color:var(--white);font-size:13px;line-height:19px}
.hero-btn{position:absolute;left:537px;top:395px;width:126px;height:32px;border:2px solid var(--white);border-radius:4px;color:var(--white);font-size:14px;font-weight:700;display:flex;align-items:center;justify-content:center}
.welcome{position:absolute;top:545px;left:0;width:1200px;height:130px;background:var(--red);color:var(--white);text-align:center}
.welcome h1{font-size:22px;font-weight:700;margin-top:5px}
.dash{border-top:1.5px dashed currentColor;margin:0 auto;width:1098px}
.welcome .dash{margin-top:10px;color:rgba(255,255,255,.85)}
.welcome p{font-size:13.5px;line-height:20px;width:1110px;margin:14px auto 0}
.offer{position:absolute;top:675px;left:0;width:1200px;height:347px;background:var(--grey-bg)}
.tabs{position:absolute;top:22px;left:224px;display:flex;gap:0}
.tab{height:44px;display:flex;align-items:center;padding:0 32px;font-size:15px;font-weight:500;color:var(--ink)}
.tab.active{border:1px solid var(--red);color:var(--red);border-radius:3px;padding:0 24px}
.offer .dash{position:absolute;top:81px;left:51px;color:#999}
.feature{position:absolute;top:116px;width:200px;margin-left:-100px;text-align:center}
.feature-img{width:140px;height:140px;border-radius:50%;margin:0 auto}
.feature h3{font-size:15px;font-weight:500;line-height:23px;margin-top:8px}
.services{position:absolute;top:1022px;left:0;width:1200px;height:317px;background:var(--white)}
.section-title{text-align:center;font-size:22px;font-weight:700;color:var(--ink)}
.section-title em{font-style:normal;color:var(--red)}
.services .section-title{margin-top:23px}
.services .dash,.news .dash{color:var(--red);margin-top:8px}
.service{position:absolute;top:119px;width:180px;margin-left:-90px;text-align:center}
.service-icon{width:94px;height:94px;border-radius:50%;background:var(--red);margin:0 auto;display:flex;align-items:center;justify-content:center}
.service-icon.current{box-shadow:inset 0 0 0 4px var(--red),inset 0 0 0 6px var(--white)}
.service h3{font-size:15px;font-weight:500;line-height:24px;margin-top:16px}
.service.current h3{color:var(--red)}
.connector{position:absolute;top:165px;height:1.5px;background:var(--red);width:68px}
.news{position:absolute;top:1339px;left:0;width:1200px;height:480px;background:var(--grey-bg)}
.news .section-title{margin-top:20px}
.post{position:absolute;top:91px;width:254px;height:356px;background:var(--white)}
.post-img{height:190px}
.post-body{padding:0 20px}
.post h3{font-size:18px;font-weight:500;margin-top:12px}
.post p{font-size:13.5px;line-height:20px;color:var(--muted);margin-top:8px;height:42px}
.post-meta{border-top:1px solid var(--line);margin-top:22px;padding-top:16px;display:flex;justify-content:space-between;font-size:12px;color:var(--muted)}
.post-meta span{display:flex;align-items:center;gap:5px}
.social-bar{position:absolute;top:1819px;left:0;width:1200px;height:73px;background:var(--white)}
.social-bar .rule{position:absolute;top:36px;left:66px;width:1068px;border-top:1px solid var(--line)}
.like-pill{position:absolute;left:376px;top:14px;width:450px;height:45px;border:1px solid var(--line);border-radius:23px;background:var(--white);display:flex;align-items:center}
.like-pill .thumb{width:58px;height:100%;border-right:1px solid var(--line);display:flex;align-items:center;justify-content:center}
.like-btn{margin-left:60px;background:#4a68ad;color:var(--white);font-size:10px;font-weight:700;padding:3px 7px;border-radius:2px}
.like-text{font-size:11px;margin-left:8px;color:#333}
.site-footer{position:absolute;top:1892px;left:0;width:1200px;height:389px;background:var(--red);color:var(--white)}
.footer-col{position:absolute;top:33px}
.footer-col h2{font-size:18px;font-weight:700}
.footer-col p{font-size:13px;line-height:19px;margin-top:15px}
.contact-col{left:52px;width:260px}
.contact-col strong{font-weight:700}
.socials{display:flex;gap:12px;margin-top:18px}
.socials span{width:13px;height:13px;border-radius:50%;background:var(--white)}
.hq-col{left:333px;width:536px;text-align:center}
.map{width:536px;height:198px;margin-top:14px;background:linear-gradient(120deg,#bfd8ea 0%,#cfe0ea 35%,#ece8dc 50%,#e8e4d8 80%,#cfe3c6 100%)}
.about-col{left:897px;width:252px}
.footer-bottom{position:absolute;top:321px;left:52px;width:1098px;border-top:1px solid rgba(255,255,255,.6);height:68px;display:flex;align-items:center;justify-content:space-between;font-size:12px;font-weight:700}
.footer-brand{display:flex;align-items:center;gap:8px;font-size:17px;font-weight:700}
.footer-brand i{width:20px;height:20px;background:var(--white);display:block}
</style>
</head>
<body>

<section class="hero">
  <div class="hero-visual" role="img" aria-label="Desert military vehicle on the left blending diagonally into an orbital view of Earth with clouds and a satellite"></div>
  <div class="hero-shade"></div>
  <header class="site-header">
    <div class="brand"><span class="brand-mark"></span>BRIGHTLENS OPTICS</div>
    <nav class="main-nav">
      <a style="left:365px">COMPANY</a>
      <a style="left:464px">SERVICES</a>
      <a style="left:563px">PRODUCTS</a>
      <a style="left:666px">NEWS</a>
      <a style="left:739px">APPLICATIONS</a>
    </nav>
    <div class="header-btn btn-contact">Contact Us</div>
    <div class="header-btn btn-quote">Request a Quote</div>
  </header>
  <h2 class="hero-title">Multispectral Technology<br>Advancement Industry Day</h2>
  <p class="hero-text">Brightlens Optics Corporation’s newest multispectral technology was demonstrated by the Federal Defense Office of the<br>Army at October’s Hyper Spectral/Multi Spectral Technology Advancement Industry Day at Alder Ridge Proving Ground, Vermont.</p>
  <div class="hero-btn">READ MORE</div>
</section>

<section class="welcome">
  <h1>Welcome to Brightlens Optics Corporation</h1>
  <div class="dash"></div>
  <p>Brightlens Optics Corporation offers a single engineering and manufacturing source for characterization, control, and exploitation of the optical properties of surfaces. Our unique understanding of customers’ needs allows us to offer engineering services, proprietary analytical software, reflectometers, hyperspectral and multispectral imagers, and surface coating products that are cost effective, innovative, and provide unsurpassed performance.</p>
</section>

<section class="offer">
  <div class="tabs">
    <div class="tab active">Coatings</div>
    <div class="tab">Measurement</div>
    <div class="tab">Spectral Imaging Systems</div>
    <div class="tab">Reflectometers and Emissometers</div>
  </div>
  <div class="dash"></div>
  <div class="feature" style="left:152px"><div class="feature-img" role="img" aria-label="Large roll-to-roll vacuum coating chamber" style="background:radial-gradient(circle,#d8dcdf,#7d8388)"></div><h3>Innovative roll-to-roll<br>coating process</h3></div>
  <div class="feature" style="left:377px"><div class="feature-img" role="img" aria-label="Earth seen from space with clouds" style="background:radial-gradient(circle,#c9d8e8,#3f6a96)"></div><h3>Coatings for Space Flight<br>Composite Reflectors</h3></div>
  <div class="feature" style="left:601px"><div class="feature-img" role="img" aria-label="Optical coating equipment rack" style="background:radial-gradient(circle,#9aa6a8,#4d5658)"></div><h3>Optical Coatings</h3></div>
  <div class="feature" style="left:826px"><div class="feature-img" role="img" aria-label="Engineer at a workstation with technical drawings" style="background:radial-gradient(circle,#b7bcc2,#4a4f57)"></div><h3>Spectrally Tailored Paint</h3></div>
  <div class="feature" style="left:1051px"><div class="feature-img" role="img" aria-label="Production facility floor with equipment" style="background:radial-gradient(circle,#e2cf86,#7d8d6e)"></div><h3>Facilities and Quality<br>Control</h3></div>
</section>

<section class="services">
  <h2 class="section-title">What <em>We Do</em></h2>
  <div class="dash"></div>
  <div class="connector" style="left:181px"></div>
  <div class="connector" style="left:367px"></div>
  <div class="connector" style="left:554px"></div>
  <div class="connector" style="left:740px"></div>
  <div class="connector" style="left:925px;width:86px"></div>
  <div class="service" style="left:132px"><div class="service-icon"><svg width="46" height="46" viewBox="0 0 46 46" fill="none" stroke="#fff" stroke-width="2"><circle cx="23" cy="23" r="7"/><circle cx="23" cy="23" r="14"/><path d="M23 4v5M23 37v5M4 23h5M37 23h5M9.6 9.6l3.5 3.5M32.9 32.9l3.5 3.5M9.6 36.4l3.5-3.5M32.9 13.1l3.5-3.5"/></svg></div><h3>R&amp;D Engineering<br>Services</h3></div>
  <div class="service" style="left:318px"><div class="service-icon"><svg width="46" height="46" viewBox="0 0 46 46" fill="none" stroke="#fff" stroke-width="2"><rect x="7" y="8" width="32" height="24"/><path d="M4 36h38M18 14v10l-3-3M18 24l3-3M28 14v10l-3-3M28 24l3-3"/></svg></div><h3>Hyperspectral and<br>Multispectral Imaging</h3></div>
  <div class="service" style="left:505px"><div class="service-icon"><svg width="46" height="46" viewBox="0 0 46 46" fill="none" stroke="#fff" stroke-width="2"><rect x="9" y="14" width="22" height="22"/><path d="M9 8h22M9 8l3-3M9 8l3 3M31 8l-3-3M31 8l-3 3M38 14v22M38 14l-3 3M38 14l3 3M38 36l-3-3M38 36l3-3"/></svg></div><h3>Optical Properties<br>Measurements</h3></div>
  <div class="service" style="left:692px"><div class="service-icon"><svg width="46" height="46" viewBox="0 0 46 46" fill="none" stroke="#fff" stroke-width="2"><circle cx="23" cy="11" r="7" fill="#fff"/><text x="23" y="15" font-size="10" font-family="Roboto,sans-serif" font-weight="700" fill="#c80c0c" stroke="none" text-anchor="middle">5</text><path d="M7 24v14h32V24M23 22v12M19 30l4 4 4-4"/></svg></div><h3>Vacuum Deposition<br>Coatings</h3></div>
  <div class="service current" style="left:876px"><div class="service-icon current"><svg width="46" height="46" viewBox="0 0 46 46" fill="none" stroke="#fff" stroke-width="2"><circle cx="23" cy="19" r="12"/><path d="M23 19l5-6M10 36h26M23 31v5"/></svg></div><h3>Reflectometer<br>Instrumentation</h3></div>
  <div class="service" style="left:1060px"><div class="service-icon"><svg width="46" height="46" viewBox="0 0 46 46" fill="none" stroke="#fff" stroke-width="2"><path d="M14 8h18l-3 10H17zM20 18v6h6v-6M22 24l-4 16h6l2-16M32 12h6"/></svg></div><h3>Pigmented<br>Coatings</h3></div>
</section>

<section class="news">
  <h2 class="section-title">Latest <em>News &amp; Views</em></h2>
  <div class="dash"></div>
  <article class="post" style="left:52px">
    <div class="post-img" role="img" aria-label="Traveller carrying a bag beside a wooden staircase" style="background:linear-gradient(90deg,#d9d4cc,#8a5a34)"></div>
    <div class="post-body"><h3>Standard Post</h3><p>Enim congue blandit. Lorem ipsum dolor sit amet, consectetur adipiscing elit. Quisque...</p>
    <div class="post-meta"><span>▦ 22 June, 2015</span><span>● 0</span></div></div>
  </article>
  <article class="post" style="left:333px">
    <div class="post-img" role="img" aria-label="Glass coffee carafe on a table" style="background:linear-gradient(90deg,#cfd0cb,#9a9c95)"></div>
    <div class="post-body"><h3>Video Post</h3><p>Ultrices posuere cubilia curae curabitur sit amet tortor ut massa commodo. Vestibulum...</p>
    <div class="post-meta"><span>▦ 22 June, 2015</span><span>● 0</span></div></div>
  </article>
  <article class="post" style="left:614px">
    <div class="post-img" role="img" aria-label="White chair and wooden table by a brick wall" style="background:linear-gradient(90deg,#7b5a45,#b58a62)"></div>
    <div class="post-body"><h3>Post with Image</h3><p>Enim congue blandit. Lorem ipsum dolor sit amet, consectetur adipiscing elit. Quisque...</p>
    <div class="post-meta"><span>▦ 22 June, 2015</span><span>● 0</span></div></div>
  </article>
  <article class="post" style="left:896px">
    <div class="post-img" role="img" aria-label="Leather wallet on a table in front of a framed collection" style="background:linear-gradient(90deg,#e5ded4,#9b7b63)"></div>
    <div class="post-body"><h3>Image Post</h3><p>Ultrices posuere cubilia curae curabitur sit amet tortor ut massa commodo. Vestibulum...</p>
    <div class="post-meta"><span>▦ 22 June, 2015</span><span>● 3</span></div></div>
  </article>
</section>

<section class="social-bar">
  <div class="rule"></div>
  <div class="like-pill">
    <div class="thumb"><svg width="18" height="18" viewBox="0 0 18 18" fill="none" stroke="#bbb" stroke-width="1.5"><path d="M2 8h3v8H2zM5 8l4-6c1.5 0 2 1 1.5 2.5L10 7h5c1 0 1.5 1 1.2 2l-1.5 5.5c-.3 1-1 1.5-2 1.5H5"/></svg></div>
    <span class="like-btn">✓ Like</span><span class="like-text">You and 4k others like this.</span>
  </div>
</section>

<footer class="site-footer">
  <div class="footer-col contact-col">
    <h2>Contact Us</h2>
    <p>Please feel free to contact us for any issue. Our staff is available to you from 9AM until 5PM on weekdays.</p>
    <p><strong>Phone:</strong> +1 800 555 0147</p>
    <p><strong>Office:</strong> Harborview Science Hall</p>
    <p><strong>Email:</strong> info@brightlens.net</p>
    <div class="socials"><span></span><span></span><span></span><span></span><span></span></div>
  </div>
  <div class="footer-col hq-col">
    <h2>Headquarters</h2>
    <div class="map" role="img" aria-label="Street map of the harbour district with the headquarters location pin"></div>
  </div>
  <div class="footer-col about-col">
    <h2>About Team</h2>
    <p>Enim congue blandit. Lorem ipsum dolor sit amet, consectetur adipiscing elit. Quisque consectetur interdum finibus. Vestibulum ante ipsum primis in faucibus orci. luctus et ultrices posuere.</p>
    <p>Cubilia cras blandit finibus ipsum, id porttitor arcu volutpat a. Integer iaculis erat nec justo malesuada faucibus vel tempus sapien. Vivamus aliquam euismod tristique.</p>
  </div>
  <div class="footer-bottom">
    <span>Copyright © 2017 Brightlens Optics Corporation</span>
    <span class="footer-brand"><i></i>BRIGHTLENS OPTICS</span>
    <span>All rights reserved</span>
  </div>
</footer>

</body>
</html>
```